Commercial snow and summer maintenance marketing folders

I'M looking to design a marketing folder for my snow and summer maintenance company.
The folder is a 12''x9'' , i want to fill up the front and back.
Acquire them for the first,keep them for all time is the slogan that will go somewhere in the front ,
I will attach logo, im thinking to having that in the front,top,middle. having a small logo in back bottom middle of page with phone number 647-319-5520,www.brindlegrounds.com . Proud members of Greenway Guild, Wise With Grit And TCPA with small logos beside them. Small writing underneath "2016 Brindle Grounds Ltd. Independently owned and operated. Propriety and Confidential
B2B, Industrial, commercial and municipal customers
Snow Removal

```html
<!DOCTYPE html>
<html lang="en">
<head>
<meta charset="utf-8">
<title>Brindle Grounds – Presentation Folder</title>
<link rel="stylesheet" href="https://fonts.googleapis.com/css2?family=Oswald:wght@600&family=Montserrat:wght@700&family=Lato:wght@400;700&display=swap">
<style>
  :root {
    --backdrop: #3b3b3b;
    --green-deep: #1f6b2e;
    --green-mid: #2d8a3e;
    --green-dark: #17502a;
    --lime: #9cc83a;
    --yellow: #e2e31f;
    --paper: #ffffff;
    --ink: #555555;
    --grass-top: #f3e6b8;
    --grass: #7fae2f;
  }
  * { margin: 0; padding: 0; box-sizing: border-box; }
  html, body { width: 907px; height: 1200px; overflow: hidden; background: var(--backdrop); }
  .canvas { position: relative; width: 907px; height: 1200px; }
  .shapes { position: absolute; inset: 0; }
  .brand {
    position: absolute; display: flex; align-items: center; justify-content: center; gap: 6px;
    font-family: "Oswald", sans-serif; font-weight: 600; color: var(--green-deep);
    letter-spacing: 2px; text-transform: uppercase; line-height: 1;
  }
  .brand-mark { background: var(--green-mid); }
  .brand--front { left: 449px; width: 353px; top: 86px; font-size: 30px; }
  .brand--front .brand-mark { width: 14px; height: 14px; }
  .brand--back { left: 96px; width: 351px; top: 372px; font-size: 17px; letter-spacing: 1.5px; }
  .brand--back .brand-mark { width: 8px; height: 8px; }
  .slogan { position: absolute; left: 449px; width: 353px; top: 160px; text-align: center; }
  .slogan-lead {
    font-family: "Montserrat", sans-serif; font-weight: 700; font-size: 15.5px;
    letter-spacing: 1px; color: var(--green-dark); text-transform: uppercase;
  }
  .slogan-main {
    font-family: "Oswald", sans-serif; font-weight: 600; font-size: 31px; line-height: 1.1;
    color: var(--green-deep); text-transform: uppercase;
  }
  .contact { position: absolute; left: 96px; width: 351px; top: 406px; text-align: center; font-family: "Lato", sans-serif; }
  .contact-phone { display: flex; align-items: center; justify-content: center; gap: 5px;
    font-weight: 700; font-size: 14px; color: var(--green-deep); }
  .contact-web { font-size: 9px; letter-spacing: 1px; color: var(--ink); margin-top: 1px; }
  .contact-members { font-size: 9px; color: var(--ink); margin-top: 4px; }
  .legal {
    position: absolute; left: 117px; width: 290px; top: 461px; height: 15px; border-radius: 8px;
    background: var(--lime); font-family: "Lato", sans-serif; font-size: 6.4px; color: var(--green-dark);
    display: flex; align-items: center; justify-content: center;
  }
</style>
</head>
<body>
<div class="canvas">
  <svg class="shapes" width="907" height="1200" viewBox="0 0 907 1200">
    <defs>
      <linearGradient id="field-dark" x1="0" y1="0" x2="0" y2="1">
        <stop offset="0" stop-color="#1c5e27"/><stop offset="1" stop-color="#2f8a3a"/>
      </linearGradient>
      <linearGradient id="field-light" x1="0" y1="0" x2="0" y2="1">
        <stop offset="0" stop-color="var(--grass-top)"/><stop offset="0.3" stop-color="#b7c85a"/><stop offset="1" stop-color="var(--grass)"/>
      </linearGradient>
      <linearGradient id="lime-glow" x1="0" y1="0" x2="1" y2="0">
        <stop offset="0" stop-color="var(--lime)"/><stop offset="1" stop-color="var(--yellow)"/>
      </linearGradient>
      <radialGradient id="pocket" cx="0.5" cy="0.5" r="0.7">
        <stop offset="0" stop-color="var(--green-mid)"/><stop offset="1" stop-color="var(--green-deep)"/>
      </radialGradient>
      <linearGradient id="fold" x1="0" y1="0" x2="1" y2="0">
        <stop offset="0" stop-color="#c8c8c8"/><stop offset="1" stop-color="#ffffff"/>
      </linearGradient>
    </defs>

    <!-- outside spread: back cover -->
    <rect x="96" y="33" width="351" height="455" fill="var(--paper)"/>
    <path d="M96 33H447V398C340 320 220 285 96 325Z" fill="url(#field-dark)" role="img" aria-label="Dark green photo of tall grass"/>
    <path d="M96 325C220 285 340 320 447 398V410C340 332 220 297 96 337Z" fill="var(--lime)"/>
    <path d="M96 337C220 297 340 332 447 410V416C340 340 220 305 96 345Z" fill="var(--green-mid)"/>

    <!-- outside spread: front cover -->
    <rect x="449" y="33" width="353" height="455" fill="var(--paper)"/>
    <rect x="449" y="240" width="353" height="200" fill="url(#field-light)" role="img" aria-label="Photo of fresh green grass at sunrise"/>
    <path d="M449 395C540 420 620 445 802 400V488H449Z" fill="url(#lime-glow)"/>
    <path d="M449 395C540 420 620 445 802 400V418C640 455 540 440 449 410Z" fill="var(--green-deep)"/>
    <path d="M449 410C540 440 640 455 802 418V424C640 462 540 446 449 416Z" fill="var(--paper)"/>

    <!-- outside pockets -->
    <path d="M96 488H447L436 647H96Z" fill="url(#pocket)"/>
    <path d="M452 488H802V647H464Z" fill="url(#pocket)"/>

    <!-- inside spread -->
    <rect x="96" y="708" width="351" height="452" fill="var(--paper)"/>
    <rect x="449" y="708" width="353" height="452" fill="var(--paper)"/>
    <rect x="449" y="708" width="60" height="300" fill="url(#fold)"/>
    <path d="M96 1005H432L446 1160H96Z" fill="url(#pocket)"/>
    <path d="M452 1005H802V1160H450Z" fill="url(#pocket)"/>
  </svg>

  <div class="brand brand--front"><span class="brand-mark"></span>Brindle Grounds</div>
  <div class="slogan">
    <p class="slogan-lead">Acquire them for the first</p>
    <p class="slogan-main">Keep them for all time</p>
  </div>

  <div class="brand brand--back"><span class="brand-mark"></span>Brindle Grounds</div>
  <div class="contact">
    <p class="contact-phone">
      <svg width="13" height="13" viewBox="0 0 24 24" aria-hidden="true"><circle cx="12" cy="12" r="10.5" fill="none" stroke="var(--green-deep)" stroke-width="2"/><path d="M8.5 6.5l2 2.5-1.2 1.5c.8 1.6 2 2.8 3.6 3.6l1.5-1.2 2.5 2-1 1.9c-4.5-.5-8.3-4.3-8.8-8.8z" fill="var(--green-deep)"/></svg>
      647-319-5520
    </p>
    <p class="contact-web">www.brindlegrounds.com</p>
    <p class="contact-members">Proud members of Greenway Guild, Wise With Grit And TCPA</p>
  </div>
  <p class="legal">2016 Brindle Grounds Ltd. Independently owned and operated. Propriety and Confidential</p>
</div>
</body>
</html>
```